IT Security Company Website

We would like to create a new look for our current company site velmora.io. The company offercyber security services for banks, goverment etc. Therefore a very professional look is important. We need at least 2 pages designed.

Target Market(s)

B2B

Coding

Coded - Design and coding required

Number of Pages Required

1 page

```html
<!DOCTYPE html>
<html lang="en">
<head>
<meta charset="utf-8">
<title>Velmora – Cyber Threat Intelligence</title>
<link href="https://fonts.googleapis.com/css2?family=Barlow+Semi+Condensed:wght@500;600;700&family=Rubik:wght@400;500&display=swap" rel="stylesheet">
<style>
:root{
  --navy-deep:#0a1158;
  --navy:#141c86;
  --navy-card:#131a6e;
  --ink:#141a5e;
  --text:#4a4d5e;
  --yellow:#f0c94a;
  --light:#f1f1f3;
  --footer:#0c0f1f;
  --white:#fff;
}
*{box-sizing:border-box;margin:0;padding:0}
html,body{width:1200px;height:3874px;overflow:hidden}
body{position:relative;font-family:"Rubik",sans-serif;color:var(--text);background:#fff}
.section{position:absolute;left:0;width:1200px}
.abs{position:absolute}
.heading{font-family:"Barlow Semi Condensed",sans-serif;font-weight:700;color:var(--ink)}
.btn{position:absolute;display:flex;align-items:center;justify-content:center;font-family:"Rubik",sans-serif;font-weight:500;font-size:13px}
.btn-yellow{background:var(--yellow);color:var(--ink)}
.btn-navy{background:var(--navy-deep);color:#fff}
.media{position:absolute}

/* hero */
.hero{top:0;height:572px;background:linear-gradient(120deg,#0c1468 0%,#0a1158 45%,#16207a 100%)}
.topbar{top:0;left:0;width:1200px;height:36px;border-bottom:1px solid rgba(255,255,255,.12);color:#fff;font-size:12px}
.topbar .item{position:absolute;top:11px;display:flex;align-items:center;gap:7px}
.social{position:absolute;display:flex;gap:14px}
.social span{width:9px;height:9px;border-radius:50%;background:#fff;display:block}
.logo{font-family:"Rubik",sans-serif;font-weight:400;color:#fff;font-size:36px;letter-spacing:1px}
.nav{top:65px;left:409px;display:flex;gap:0;font-size:12.5px;font-weight:500;color:#fff}
.nav a{color:#fff;text-decoration:none;position:absolute;white-space:nowrap}
.nav a.active{color:var(--yellow)}
.header-line{top:110px;left:0;width:1200px;height:1px;background:rgba(255,255,255,.1)}
.hero-kicker{left:87px;top:204px;font-family:"Barlow Semi Condensed",sans-serif;font-weight:500;font-size:24px;color:var(--yellow)}
.hero-title{left:87px;top:236px;font-family:"Barlow Semi Condensed",sans-serif;font-weight:700;font-size:55px;line-height:60px;color:#fff}
.hero-title em{font-style:normal;color:var(--yellow)}
.demo{left:808px;top:197px;width:313px;height:271px;background:var(--navy)}
.demo h3{position:absolute;left:31px;top:26px;font-family:"Barlow Semi Condensed",sans-serif;font-weight:700;font-size:25px;line-height:32px;color:#fff}
.demo .field{position:absolute;left:31px;top:104px;width:249px;height:33px;background:#fff;font-size:10px;color:#8a8c99;padding:10px 15px}
.demo .check{position:absolute;left:31px;top:153px;width:17px;height:17px;background:#fff;border-radius:2px}
.demo .agree{position:absolute;left:56px;top:153px;font-size:10px;line-height:16px;color:#fff}
.banner{left:275px;top:541px;width:648px;height:58px;background:var(--yellow);font-family:"Barlow Semi Condensed",sans-serif;font-weight:700;font-size:20px;color:var(--ink);display:flex;align-items:center;justify-content:center;letter-spacing:.3px}

/* about */
.about{top:572px;height:580px}
.framed{box-shadow:0 0 0 5px #fff,0 4px 18px rgba(0,0,0,.18)}
.about .photo{left:90px;top:117px;width:476px;height:381px;background:linear-gradient(135deg,#1a2f6e,#2b5aa8 55%,#10214f)}
.about h2{left:639px;top:128px;font-size:34px;line-height:39px}
.about p{left:639px;top:228px;width:460px;font-size:13.5px;line-height:21px}
.checklist{left:639px;top:395px;list-style:none;font-size:13.5px;line-height:24px}
.checklist li{display:flex;align-items:center;gap:10px}

/* news */
.news{top:1152px;height:519px;background:linear-gradient(160deg,#17208a,#101877)}
.news h2{left:0;width:1200px;text-align:center;top:70px;font-size:33px;color:#fff}
.news-card{top:145px;width:421px;height:229px;background:#fff}
.news-card .day{position:absolute;left:24px;top:28px;font-family:"Rubik",sans-serif;font-weight:500;font-size:30px;color:var(--navy-deep)}
.news-card .mon{position:absolute;left:21px;top:65px;font-size:11px;color:#222}
.news-card h3{position:absolute;left:95px;top:27px;width:300px;font-family:"Rubik",sans-serif;font-weight:500;font-size:19px;line-height:24px;color:#111}
.news-card p{position:absolute;left:95px;top:90px;width:300px;font-size:11.5px;line-height:17.5px;color:#555}
.news-card .by{position:absolute;left:90px;top:173px;font-size:11.5px;color:var(--yellow)}
.news-card .btn{left:278px;top:164px;width:108px;height:32px;font-size:12px}
.arrow{top:1397px}
.view-all-outline{left:546px;top:405px;width:108px;height:33px;border:1.5px solid var(--yellow);color:var(--yellow);background:transparent}

/* ciso */
.ciso{top:1671px;height:481px}
.ciso h2{left:87px;top:102px;font-size:34px;line-height:39px}
.ciso p{left:87px;top:199px;width:668px;font-size:13.5px;line-height:21px}
.ciso .photo{left:811px;top:89px;width:306px;height:308px;background:linear-gradient(140deg,#0c1a2e,#1c3d6a 55%,#0a1526)}

/* risks */
.risks{top:2152px;height:1002px;background:var(--light)}
.risks h2{left:0;width:1200px;text-align:center;top:73px;font-size:34px}
.risk{overflow:hidden}
.risk .shade{position:absolute;inset:0;background:linear-gradient(180deg,rgba(0,0,0,0) 35%,rgba(0,0,0,.82) 100%)}
.risk h3{position:absolute;left:23px;top:217px;font-family:"Rubik",sans-serif;font-weight:500;font-size:15px;color:#fff}
.risk p{position:absolute;left:23px;top:248px;width:calc(100% - 46px);font-size:11.5px;line-height:19px;color:#d5d6dc}
.risk .more{position:absolute;left:23px;top:300px;font-size:12px;color:var(--yellow)}
.risk.solid{background:var(--navy-card)}
.risk.solid h3,.risk.solid p{color:var(--yellow)}
.risks .view-all{left:546px;top:888px;width:108px;height:33px}

/* founders */
.founders{top:3154px;height:373px}
.founders h2{left:0;width:1200px;text-align:center;top:72px;font-size:34px}
.portrait{top:155px;width:130px;height:135px;background:linear-gradient(180deg,#d8d8d8,#8c8c8c);border:2px solid #e4e4e4}
.founder-name{font-family:"Barlow Semi Condensed",sans-serif;font-weight:700;font-size:17px;color:var(--ink)}
.founder-role{font-size:12px;color:var(--yellow)}
.founder-bio{font-family:"Barlow Semi Condensed",sans-serif;font-weight:500;font-size:15px;line-height:19px;color:#333}

/* footer */
.footer{top:3527px;height:305px;background:radial-gradient(circle at 15% 40%,#1a1f3a,var(--footer) 60%)}
.footer h4{position:absolute;top:74px;font-family:"Barlow Semi Condensed",sans-serif;font-weight:700;font-size:16px;color:var(--yellow)}
.footer .links{position:absolute;left:369px;top:106px;list-style:none;font-size:13.5px;line-height:25px;color:#fff}
.footer .links li:first-child{text-decoration:underline;color:var(--yellow)}
.contact{position:absolute;left:543px;font-size:13.5px;line-height:19px;color:#fff;display:flex;gap:12px}
.sub-field{left:839px;top:111px;width:272px;height:38px;background:#fff;font-size:12px;color:#555;display:flex;align-items:center;gap:10px;padding-left:16px}
.sign-up{left:839px;top:165px;width:113px;height:38px}
.to-top{left:1128px;top:232px;width:42px;height:42px;border-radius:50%;background:var(--yellow);display:flex;align-items:center;justify-content:center}
.copyright{top:3832px;height:42px;background:#1a2494;color:#fff;font-size:13px;display:flex;align-items:center;justify-content:center}
</style>
</head>
<body>

<header class="section hero">
  <div class="abs topbar">
    <div class="item" style="left:88px">
      <svg width="12" height="12" viewBox="0 0 24 24" fill="none" stroke="#f0c94a" stroke-width="2"><path d="M22 16.9v3a2 2 0 0 1-2.2 2 19.8 19.8 0 0 1-8.6-3.1 19.5 19.5 0 0 1-6-6A19.8 19.8 0 0 1 2.1 4.2 2 2 0 0 1 4.1 2h3a2 2 0 0 1 2 1.7c.1.9.4 1.8.7 2.7a2 2 0 0 1-.5 2.1L8 9.8a16 16 0 0 0 6 6l1.3-1.3a2 2 0 0 1 2.1-.4c.9.3 1.8.6 2.7.7a2 2 0 0 1 1.7 2z"/></svg>
      +41 700 000 111 / +1 555 010 2244
    </div>
    <div class="item" style="left:322px">
      <svg width="13" height="11" viewBox="0 0 24 18" fill="none" stroke="#f0c94a" stroke-width="2"><rect x="1" y="1" width="22" height="16" rx="1"/><path d="M1 1l11 9 11-9"/></svg>
      info@velmora.io
    </div>
    <div class="social" style="left:1029px;top:14px"><span></span><span></span><span></span><span></span></div>
  </div>

  <div class="abs logo" style="left:87px;top:53px">VELMORA</div>
  <nav class="abs nav">
    <a class="active" style="left:0;top:0">Home</a>
    <a style="left:72px;top:0">Q&amp;A</a>
    <a style="left:134px;top:0">Pricing</a>
    <a style="left:215px;top:0">About Us</a>
    <a style="left:305px;top:0">Contact</a>
    <a style="left:391px;top:0">Resources</a>
  </nav>
  <div class="btn btn-yellow" style="left:996px;top:59px;width:125px;height:33px;font-size:12.5px">Quick Inquiry</div>
  <div class="abs header-line"></div>

  <div class="abs hero-kicker">We Understand Security:</div>
  <h1 class="abs hero-title">We Have Been Active In<br>The Cyber Security<br>Sector For Over <em>20 Years</em></h1>

  <form class="abs demo">
    <h3>Arrange a live<br>demo today!</h3>
    <div class="field">Enter your E-mail here</div>
    <div class="check"></div>
    <div class="agree">I agree that my data is stored for<br>the purpose of a live demo</div>
    <div class="btn btn-yellow" style="left:31px;top:205px;width:109px;height:33px;font-size:12.5px">Submit</div>
  </form>

  <div class="abs banner">VELMORA: CREATED FOR SWISS BANKS, PRICED FOR MSSP</div>
</header>

<section class="section about">
  <div class="media photo framed" role="img" aria-label="Security analyst with a headset working at a computer"></div>
  <h2 class="abs heading">Defend Against Cyber-Attacks<br>Before They Happen</h2>
  <p class="abs">Velmora helps you understand when, where and how stolen or accidentally leaked information in dark web markets, forums, botnet logs, IRC, social media and other sources is exposed. Velmora's alerting service can also detect threats before they turn into incidents. Velmora offers AI-driven dark web analysis, real-time threat alerts and pre-Attack threat indicators. Setup in minutes you will receive instant access to real-time reporting including:</p>
  <ul class="abs checklist">
    <li><svg width="12" height="10" viewBox="0 0 12 10" fill="none" stroke="#f0c94a" stroke-width="1.6"><path d="M0 5h11M7 1l4 4-4 4"/></svg>Infrastructure exposure: IOT, code repos, cloud hosting &amp; more</li>
    <li><svg width="12" height="10" viewBox="0 0 12 10" fill="none" stroke="#f0c94a" stroke-width="1.6"><path d="M0 5h11M7 1l4 4-4 4"/></svg>People exposure: Social media monitoring</li>
    <li><svg width="12" height="10" viewBox="0 0 12 10" fill="none" stroke="#f0c94a" stroke-width="1.6"><path d="M0 5h11M7 1l4 4-4 4"/></svg>Ransomware exposure: leak &amp; credential monitoring</li>
    <li><svg width="12" height="10" viewBox="0 0 12 10" fill="none" stroke="#f0c94a" stroke-width="1.6"><path d="M0 5h11M7 1l4 4-4 4"/></svg>Attack prevention: domain and certificate monitoring</li>
  </ul>
</section>

<section class="section news">
  <h2 class="abs heading">Cyber Threat Intelligence News</h2>
  <svg class="abs" style="left:115px;top:232px" width="28" height="28" viewBox="0 0 28 28" fill="none" stroke="#3b4fc4" stroke-width="2"><rect x="1" y="1" width="26" height="26" rx="7"/><path d="M19 14H9M13 9l-5 5 5 5"/></svg>
  <svg class="abs" style="left:1057px;top:232px" width="28" height="28" viewBox="0 0 28 28" fill="none" stroke="#f0c94a" stroke-width="2"><rect x="1" y="1" width="26" height="26" rx="7"/><path d="M9 14h10M15 9l5 5-5 5"/></svg>

  <article class="abs news-card" style="left:167px">
    <div class="day">19</div><div class="mon">Jun. 22</div>
    <h3>Norvane banking solution hacked, data leaked online</h3>
    <p>Norvane is an Irish-owned banking software company which provides mobile, internet and ATM financial service technology to more than...</p>
    <div class="by">- Velmora AG</div>
    <div class="btn btn-navy">Read More</div>
  </article>
  <article class="abs news-card" style="left:612px">
    <div class="day">14</div><div class="mon">Jun. 22</div>
    <h3>Chatterly social network data breach</h3>
    <p>Southeast Asia's 1st social media &amp; messaging super app that connects people around the world with multi-features, including social...</p>
    <div class="by">- Velmora AG</div>
    <div class="btn btn-yellow">Read More</div>
  </article>

  <div class="btn view-all-outline">View All</div>
</section>

<section class="section ciso">
  <h2 class="abs heading">The CISO's Solution –<br>forewarned is forearmed.</h2>
  <p class="abs">Velmora helps you understand when, where and how stolen or accidentally leaked information is exposed. Velmora's alerting service can also detect threats before they turn into incidents. There are certain indicators that can be measured. Before an attack takes place, hackers often reserve similar domain names (typosquatting), they spoof profiles in social media like professional networks or they exchange information about targets in hacker forums. Velmora monitors these activities using "Social Media Monitoring", "Domain Monitoring" and the "Hacker Forum Monitoring". Velmora's Intelligent Filters and Machine Learning find the real risks among the vast amount of data we collect through human and machine intelligence.</p>
  <div class="media photo framed" role="img" aria-label="Hands typing on a laptop with a glowing security shield overlay"></div>
</section>

<section class="section risks">
  <h2 class="abs heading">What risks can be mitigated with Velmora?</h2>

  <article class="abs risk" style="left:87px;top:145px;width:387px;height:337px">
    <div class="media" style="inset:0;background:linear-gradient(135deg,#3a2418,#1e1410 60%,#120c0a)" role="img" aria-label="Padlock and login form graphic representing phishing"></div>
    <div class="shade"></div>
    <h3>Prevent phishing</h3>
    <p>We monitor all new domain registrations (ccTLDs, gTLDs, uTLD, sTLD). In doing so, we also record...</p>
    <div class="more">Read More</div>
  </article>
  <article class="abs risk" style="left:498px;top:145px;width:299px;height:337px">
    <div class="media" style="inset:0;background:linear-gradient(135deg,#2c4460,#1a2838 60%,#0e151f)" role="img" aria-label="Two engineers reviewing a tablet in a server room"></div>
    <div class="shade"></div>
    <h3>Detect exposed infrastructure</h3>
    <p>We monitor server access, IOT (public scanners) or complete DB dumps in different...</p>
    <div class="more">Read More</div>
  </article>
  <article class="abs risk" style="left:821px;top:145px;width:300px;height:337px">
    <div class="media" style="inset:0;background:linear-gradient(135deg,#1f5c70,#12303c 55%,#0a161c)" role="img" aria-label="Hooded figure in front of binary code"></div>
    <div class="shade"></div>
    <h3>Detect leaks from ransomware</h3>
    <p>In ransomware attacks, victims are black-mailed into paying a ransom sum in...</p>
    <div class="more">Read More</div>
  </article>

  <article class="abs risk" style="left:87px;top:505px;width:300px;height:339px">
    <div class="media" style="inset:0;background:linear-gradient(135deg,#1c3a5c,#10233a 55%,#0a1422)" role="img" aria-label="Smartphone with lock icon lying on a keyboard"></div>
    <div class="shade"></div>
    <h3>Find exposed data in the darknet</h3>
    <p>Monitoring whether your organisation's name appears in Dark Web forums...</p>
    <div class="more">Read More</div>
  </article>
  <article class="abs risk" style="left:411px;top:505px;width:299px;height:339px">
    <div class="media" style="inset:0;background:linear-gradient(135deg,#3d6fa8,#8a4a6a 50%,#1e2a44)" role="img" aria-label="Cubes printed with social media style app icons"></div>
    <div class="shade"></div>
    <h3>Detect spoofing and Impersonation</h3>
    <p>We monitor social media services such as forums, video sites, messengers...</p>
    <div class="more">Read More</div>
  </article>
  <article class="abs risk solid" style="left:734px;top:505px;width:387px;height:339px">
    <h3>Understand employee exposure</h3>
    <p>Employees who are heavily exposed to the Internet are at greater risk of social engineering attacks...</p>
    <div class="more">Read More</div>
  </article>

  <div class="btn btn-yellow view-all">View All</div>
</section>

<section class="section founders">
  <h2 class="abs heading">Founder Team</h2>
  <div class="media portrait" style="left:203px" role="img" aria-label="Portrait photo of the founder"></div>
  <div class="abs" style="left:358px;top:190px">
    <div class="founder-name">Lukas Brenner</div>
    <div class="founder-role" style="margin-top:3px">Founder</div>
    <div class="founder-bio" style="margin-top:5px">Pentester and security evangelist</div>
  </div>
  <div class="media portrait" style="left:635px" role="img" aria-label="Portrait photo of the co-founder"></div>
  <div class="abs" style="left:790px;top:178px;width:200px">
    <div class="founder-name">Marco Keller</div>
    <div class="founder-role" style="margin-top:3px">Co-Founder</div>
    <div class="founder-bio" style="margin-top:5px">Security expert and software magician</div>
  </div>
</section>

<footer class="section footer">
  <div class="abs logo" style="left:87px;top:124px;font-size:50px;letter-spacing:1px">VELMORA</div>
  <div class="social" style="left:122px;top:199px;gap:28px"><span></span><span></span><span></span><span></span></div>

  <h4 style="left:369px">QUICK LINK</h4>
  <ul class="links">
    <li>Home</li><li>Q&amp;A</li><li>Pricing</li><li>About Us</li><li>Contact</li><li>Resources</li>
  </ul>

  <h4 style="left:543px">CONTACT INFO</h4>
  <div class="contact" style="top:108px">
    <svg width="13" height="16" viewBox="0 0 24 30" fill="#f0c94a"><path d="M12 0C5.4 0 0 5.2 0 11.7 0 20.5 12 30 12 30s12-9.5 12-18.3C24 5.2 18.6 0 12 0zm0 16a4.5 4.5 0 1 1 0-9 4.5 4.5 0 0 1 0 9z"/></svg>
    <div>Velmora AG, Lindenweg 12,<br>6300 Zug, Switzerland</div>
  </div>
  <div class="contact" style="top:162px">
    <svg width="13" height="13" viewBox="0 0 24 24" fill="#f0c94a"><path d="M22 16.9v3a2 2 0 0 1-2.2 2 19.8 19.8 0 0 1-8.6-3.1 19.5 19.5 0 0 1-6-6A19.8 19.8 0 0 1 2.1 4.2 2 2 0 0 1 4.1 2h3a2 2 0 0 1 2 1.7c.1.9.4 1.8.7 2.7a2 2 0 0 1-.5 2.1L8 9.8a16 16 0 0 0 6 6l1.3-1.3a2 2 0 0 1 2.1-.4c.9.3 1.8.6 2.7.7a2 2 0 0 1 1.7 2z"/></svg>
    <div>+41 700 000 111<br>+1 555 010 2244</div>
  </div>
  <div class="contact" style="top:219px">
    <svg width="14" height="11" viewBox="0 0 24 18" fill="#f0c94a"><path d="M0 0h24v18H0z"/><path d="M0 0l12 9 12-9" stroke="#0c0f1f" stroke-width="2" fill="none"/></svg>
    <div>info@velmora.io</div>
  </div>

  <h4 style="left:839px;top:72px">STAY CONNECTED!</h4>
  <div class="abs sub-field">
    <svg width="18" height="13" viewBox="0 0 24 18" fill="none" stroke="#b9bcd0" stroke-width="1.5"><rect x="1" y="1" width="22" height="16"/><path d="M1 1l11 9 11-9"/></svg>
    name@email.com
  </div>
  <div class="btn btn-yellow sign-up">Sign Up</div>

  <div class="abs to-top">
    <svg width="14" height="16" viewBox="0 0 14 16" fill="none" stroke="#fff" stroke-width="2"><path d="M7 15V2M1 8l6-6 6 6"/></svg>
  </div>
</footer>

<div class="section copyright">Copyright © VELMORA. All Rights Reserved</div>

</body>
</html>
```